Harbor Lights (title of music CD cover)

Create a CD jacket (front and back). Front artwork will be used on CD itself.The CD is an EP (6 songs). They are all love songs (Ballads). Violin, cello, piano, percussion, acoustic guitar, that sort of sound. I am looking for a sophisticated look to the CD. The title is Harbor Lights and the subtitle is The Song of Two. The picture is of me; Lia Brandt. I want this CD jacket to exude class. I have uploaded an example of what i think i want. Obviously rough on my part.

Besides the attached picture of me, I am looking for: my name, name of Cd (Harbor Lights) and subtitle (The Song of Two)
on front of CD

Back:
1. Every Star Grew Quiet (Lia Brandt) 3:26
2. Like Fresh Rain (Lia Brandt) 3:20
3. Once Again Near (Lia Brandt) 4:00
4. The Evening (Lia Brandt) 3:53
5. Here & Always (Lia Brandt) 3:27
6. Harbor Lights (Lia Brandt / Dean Morrow) 4:28
Producer: Dean Morrow
© 2017 Blue Meadow Ventures, LLC

I have some more to go on back: barcode, publishing, additional credits
Updates

Target Market(s)

Adults 25-55

Industry/Entity Type

Music Download

Colors

Designer to choose colors to be used in the design.

Requirements
Must have
• Pic of me on front with title, subtitle and my name

```html
<!DOCTYPE html>
<html lang="en">
<head>
<meta charset="utf-8">
<title>Harbor Lights – The Song of Two – CD Cover</title>
<link rel="stylesheet" href="https://fonts.googleapis.com/css2?family=Kaushan+Script&family=Open+Sans:wght@300;400;700&display=swap">
<style>
  :root {
    --stage: #e4e5e7;
    --cover-dark: #141110;
    --cover-brown: #2a211c;
    --band-red: #3a1f1c;
    --band-red-deep: #2b1715;
    --portrait-light: #c4ab74;
    --portrait-mid: #8a7248;
    --portrait-dark: #3d3222;
    --gold: #d6a94a;
    --accent-red: #c0392b;
    --ink-white: #ffffff;
    --mic-tone: #3b302b;
  }
  * { margin: 0; padding: 0; box-sizing: border-box; }
  html, body {
    width: 1200px;
    height: 849px;
    overflow: hidden;
    background: var(--stage);
  }
  .cover {
    position: absolute;
    left: 280px;
    top: 105px;
    width: 640px;
    height: 640px;
    overflow: hidden;
    background: linear-gradient(160deg, var(--cover-brown) 0%, var(--cover-dark) 55%, #1b1513 100%);
    font-family: "Open Sans", sans-serif;
  }
  .cover__bands {
    position: absolute;
    inset: 0;
    width: 100%;
    height: 100%;
  }
  .cover__microphone {
    position: absolute;
    left: 470px;
    top: 220px;
    width: 160px;
    height: 420px;
    border-radius: 80px 80px 0 0;
    background: linear-gradient(180deg, var(--mic-tone) 0%, rgba(59, 48, 43, 0.4) 100%);
    opacity: 0.75;
  }
  .cover__portrait {
    position: absolute;
    left: 40px;
    top: 160px;
    width: 400px;
    height: 480px;
    border-radius: 200px 200px 0 0;
    background:
      radial-gradient(ellipse 60% 45% at 55% 40%, var(--portrait-light) 0%, var(--portrait-mid) 55%, transparent 100%),
      linear-gradient(180deg, var(--portrait-mid) 0%, var(--portrait-dark) 100%);
  }
  .cover__title {
    position: absolute;
    left: 100px;
    top: 50px;
    font-family: "Kaushan Script", cursive;
    font-weight: 400;
    font-size: 76px;
    line-height: 1;
    color: var(--ink-white);
    white-space: nowrap;
  }
  .cover__subtitle {
    position: absolute;
    right: 95px;
    top: 138px;
    font-size: 19px;
    font-weight: 400;
    color: var(--gold);
    white-space: nowrap;
  }
  .cover__artist {
    position: absolute;
    left: 455px;
    top: 330px;
    height: 110px;
    padding-left: 16px;
    border-left: 1.5px solid var(--gold);
  }
  .cover__artist-marker {
    position: absolute;
    left: -9px;
    top: 31px;
    width: 0;
    height: 0;
    border-top: 6px solid transparent;
    border-bottom: 6px solid transparent;
    border-right: 8px solid var(--accent-red);
  }
  .cover__artist-name {
    margin-top: 22px;
    font-size: 26px;
    color: var(--ink-white);
    white-space: nowrap;
  }
  .cover__artist-first { font-weight: 300; }
  .cover__artist-last { font-weight: 700; }
</style>
</head>
<body>
  <main class="cover">
    <svg class="cover__bands" viewBox="0 0 640 640" aria-hidden="true">
      <polygon points="0,40 150,0 230,0 0,80" fill="var(--band-red)" opacity="0.8"/>
      <polygon points="0,95 60,80 0,130" fill="var(--band-red-deep)" opacity="0.8"/>
      <polygon points="640,300 640,420 420,640 330,640" fill="var(--band-red)" opacity="0.85"/>
      <polygon points="640,460 640,640 460,640" fill="var(--band-red-deep)" opacity="0.9"/>
    </svg>
    <div class="cover__microphone" role="img" aria-label="Outline drawing of a vintage studio microphone"></div>
    <div class="cover__portrait" role="img" aria-label="Sepia-toned head-and-shoulders portrait photograph of the artist Lia Brandt with splattered paint edges"></div>
    <h1 class="cover__title">Harbor Lights</h1>
    <p class="cover__subtitle">The Song of Two</p>
    <div class="cover__artist">
      <span class="cover__artist-marker"></span>
      <p class="cover__artist-name"><span class="cover__artist-first">Lia </span><span class="cover__artist-last">Brandt</span></p>
    </div>
  </main>
</body>
</html>
```